Lanternleaf - Fresh Asian Cuisine Menu

We need to redo our menu to include pictures of food items. Our restaurant is vibrant, trendy, upscale Chinese cuisine

Requirements
Must have
• Must fit on 8.5x11 paper. We can remove the About Us section if needed but menu cannot be more than 6 pages total. Must include pictures of menu items

```html
<!DOCTYPE html>
<html lang="en">
<head>
<meta charset="utf-8">
<title>Lanternleaf - Fresh Asian Cuisine | Lunch Menu</title>
<link href="https://fonts.googleapis.com/css2?family=Crimson+Text:wght@400;600;700&display=swap" rel="stylesheet">
<style>
  :root {
    --ink: #111111;
    --body: #1e1e1e;
    --brand-red: #8e1b1f;
    --chili: #d4161b;
    --paper: #ffffff;
  }
  * { box-sizing: border-box; margin: 0; padding: 0; }
  html, body { width: 880px; height: 1200px; overflow: hidden; background: var(--paper); }
  body { font-family: "Crimson Text", Georgia, serif; color: var(--body); position: relative; }

  .masthead { position: absolute; top: 58px; left: 145px; height: 80px; width: 700px; }
  .brand { position: absolute; left: 0; top: 0; width: 280px; display: flex; flex-direction: column; align-items: flex-end; }
  .brand-name { display: flex; align-items: center; gap: 8px; font-size: 40px; font-weight: 700; color: var(--ink); letter-spacing: 0.5px; line-height: 1; margin-top: 22px; }
  .brand-name .dot { width: 16px; height: 16px; border-radius: 50%; background: var(--brand-red); }
  .brand-tagline { font-size: 13px; font-weight: 700; color: var(--brand-red); letter-spacing: 1.2px; margin-top: 4px; }
  .divider { position: absolute; left: 300px; top: 24px; width: 4px; height: 48px; background: var(--ink); }
  .menu-title { position: absolute; left: 326px; top: 18px; }
  .menu-title h1 { font-size: 30px; font-weight: 700; color: var(--ink); letter-spacing: 0.8px; line-height: 1; }
  .menu-title p { font-size: 17.5px; color: var(--ink); margin-top: 5px; }

  .column { position: absolute; top: 215px; width: 385px; }
  .column.left { left: 38px; }
  .column.right { left: 461px; }
  .item { display: flex; height: 89px; }
  .thumb { flex: 0 0 112px; height: 75px; border: 1.5px solid var(--brand-red); border-radius: 11px; }
  .thumb.house { background: var(--paper); display: flex; align-items: center; justify-content: center; gap: 4px; }
  .thumb.house .mark { width: 9px; height: 9px; border-radius: 50%; background: var(--brand-red); }
  .thumb.house span { font-size: 13px; font-weight: 700; color: var(--brand-red); }
  .info { flex: 0 0 236px; margin-left: 7px; }
  .info h2 { font-size: 16.5px; font-weight: 700; color: var(--ink); line-height: 1.15; margin-top: 4px; display: flex; align-items: center; gap: 3px; flex-wrap: wrap; }
  .info h2.plain { font-weight: 400; }
  .info p { font-size: 12.6px; line-height: 16.5px; margin-top: 1px; }
  .price { flex: 1; text-align: right; font-size: 16.5px; color: var(--ink); margin-top: 4px; padding-right: 2px; }
  .chili { width: 14px; height: 14px; }
</style>
</head>
<body>
<svg width="0" height="0" style="position:absolute">
  <symbol id="chili" viewBox="0 0 20 20">
    <path d="M16 3c1 1 1 2 0 3C13 11 8 16 2 17c3-3 7-7 10-11 1-1 2-2 4-3z" fill="var(--chili)"/>
    <path d="M15 4c1-2 2-3 4-3" stroke="#2f7a2f" stroke-width="1.6" fill="none"/>
  </symbol>
</svg>

<header class="masthead">
  <div class="brand">
    <div class="brand-name"><span class="dot"></span>LANTERNLEAF</div>
    <div class="brand-tagline">FRESH ASIAN CUISINE</div>
  </div>
  <div class="divider"></div>
  <div class="menu-title">
    <h1>LUNCH MENU</h1>
    <p>Available Monday-Friday from 11am to 3pm</p>
  </div>
</header>

<section class="column left">
  <article class="item">
    <div class="thumb" role="img" aria-label="Photo of Kung Pao Chicken" style="background:linear-gradient(135deg,#3a4a66,#7a4a2a 55%,#2c3448)"></div>
    <div class="info"><h2>Kung Pao Chicken <svg class="chili"><use href="#chili"/></svg></h2><p>Chicken sautéed with roasted peanuts and dry red chili in Kung Pao sauce</p></div>
    <div class="price">$10</div>
  </article>
  <article class="item">
    <div class="thumb" role="img" aria-label="Photo of Orange Chicken" style="background:radial-gradient(circle,#8a3a1a 30%,#e9e2d8 60%,#b8a48a)"></div>
    <div class="info"><h2>Orange Chicken</h2><p>Battered-fried chicken breast with dried chili peppers and stir fried in a tangy orange flavored sauce</p></div>
    <div class="price">$10</div>
  </article>
  <article class="item">
    <div class="thumb" role="img" aria-label="Photo of Crispy Spicy Chicken" style="background:radial-gradient(circle,#b8662a 35%,#e8e4de 62%,#6e6458)"></div>
    <div class="info"><h2>Crispy Spicy Chicken <svg class="chili"><use href="#chili"/></svg><svg class="chili"><use href="#chili"/></svg></h2><p>Crispy-diced chicken with Sichuan peppers, garlic, scallions and red and green bell peppers</p></div>
    <div class="price">$11</div>
  </article>
  <article class="item">
    <div class="thumb" role="img" aria-label="Photo of General Tso's Chicken" style="background:radial-gradient(circle,#4a2a1a 30%,#e6e2dc 60%,#5a4a3e)"></div>
    <div class="info"><h2>General Tso’s Chicken <svg class="chili"><use href="#chili"/></svg></h2><p>Battered-fried chicken breast, stir fried in a sweet &amp; tangy chili sauce with chili peppers</p></div>
    <div class="price">$10</div>
  </article>
  <article class="item">
    <div class="thumb" role="img" aria-label="Photo of Sweet and Sour Chicken" style="background:linear-gradient(135deg,#c8a27a,#e08a3a 45%,#efe8de 75%,#c03a30)"></div>
    <div class="info"><h2>Sweet &amp; Sour Chicken</h2><p>Crispy Chicken with green bell peppers, onions and pineapple glazed in a homemade sweet and sour marinade</p></div>
    <div class="price">$10</div>
  </article>
  <article class="item">
    <div class="thumb" role="img" aria-label="Photo of Oyster Beef" style="background:radial-gradient(circle,#4a2e22 28%,#ece8e2 58%,#7a6652)"></div>
    <div class="info"><h2>Oyster Beef</h2><p>Tender cuts of steak wok fried with onions and marinated in a homemade oyster sauce</p></div>
    <div class="price">$11</div>
  </article>
  <article class="item">
    <div class="thumb house"><span class="mark"></span><span>Lanternleaf</span></div>
    <div class="info"><h2>Black Pepper Steak <svg class="chili"><use href="#chili"/></svg></h2><p>Tender cuts of steak mixed with onions and red and green bell peppers</p></div>
    <div class="price">$12</div>
  </article>
  <article class="item">
    <div class="thumb" role="img" aria-label="Photo of Dancing Pork Belly" style="background:linear-gradient(135deg,#3a4a2a,#c9b894 40%,#5a2e1e 75%,#2e3a22)"></div>
    <div class="info"><h2>Dancing Pork Belly</h2><p>Braised Pork Belly on sizzling rice cracker</p></div>
    <div class="price">$12</div>
  </article>
  <article class="item">
    <div class="thumb" role="img" aria-label="Photo of Twice Cooked Pork" style="background:radial-gradient(circle,#b07a3a 32%,#e8e2d8 60%,#6a5a48)"></div>
    <div class="info"><h2>Twice Cooked Pork <svg class="chili"><use href="#chili"/></svg></h2><p>Stir fried Pork Belly slices with leek and fermented black beans</p></div>
    <div class="price">$11</div>
  </article>
  <article class="item">
    <div class="thumb" role="img" aria-label="Photo of Shredded Chicken in Spicy Garlic Sauce" style="background:radial-gradient(circle,#7a3a1e 32%,#e6e0d8 60%,#4a4038)"></div>
    <div class="info"><h2>Shredded Chicken in Spicy Garlic Sauce <svg class="chili"><use href="#chili"/></svg></h2><p>Tender shredded chicken, wood ear mushrooms, bamboo shoots, broccoli, green and red bell peppers and Chinese water chestnuts in a classic spicy garlic sauce</p></div>
    <div class="price">$11</div>
  </article>
</section>

<section class="column right">
  <article class="item">
    <div class="thumb" role="img" aria-label="Photo of Lemon Peel Shrimp" style="background:radial-gradient(circle,#e8763a 30%,#d8d0b0 58%,#b08a5a)"></div>
    <div class="info"><h2>Lemon Peel Shrimp</h2><p>Shrimp with fresh lemons in a sweet lemon sauce on a bed of shredded lettuce</p></div>
    <div class="price">$12</div>
  </article>
  <article class="item">
    <div class="thumb house"><span class="mark"></span><span>Lanternleaf</span></div>
    <div class="info"><h2>Rice Wine Fish <svg class="chili"><use href="#chili"/></svg></h2><p>White fish filet with rice wine mixed with onions, peas and carrots</p></div>
    <div class="price">$11</div>
  </article>
  <article class="item">
    <div class="thumb house"><span class="mark"></span><span>Lanternleaf</span></div>
    <div class="info"><h2>Lanternleaf Fried Rice</h2><p>Shrimp, chicken, and beef, farm fresh eggs, onions, and scallions</p></div>
    <div class="price">$10</div>
  </article>
  <article class="item">
    <div class="thumb house"><span class="mark"></span><span>Lanternleaf</span></div>
    <div class="info"><h2>Vegetarian White Fried Rice</h2><p>Mixed vegetables with white rice</p></div>
    <div class="price">$9</div>
  </article>
  <article class="item">
    <div class="thumb house"><span class="mark"></span><span>Lanternleaf</span></div>
    <div class="info"><h2>Lanternleaf Lo Mein</h2><p>Shrimp, chicken, and beef, farm fresh eggs, onions, and scallions</p></div>
    <div class="price">$10</div>
  </article>
  <article class="item">
    <div class="thumb house"><span class="mark"></span><span>Lanternleaf</span></div>
    <div class="info"><h2>Vegetarian Lo Mein</h2><p>Mixed vegetables with lo mein noodles</p></div>
    <div class="price">$9</div>
  </article>
  <article class="item">
    <div class="thumb" role="img" aria-label="Photo of Mapo Tofu" style="background:radial-gradient(circle,#b0502a 28%,#e8e4de 55%,#1e1e1e 72%)"></div>
    <div class="info"><h2>Mapo Tofu <svg class="chili"><use href="#chili"/></svg><svg class="chili"><use href="#chili"/></svg></h2><p>Soft Tofu, scallion, Sichuan peppercorn and peppers</p></div>
    <div class="price">$9</div>
  </article>
  <article class="item">
    <div class="thumb" role="img" aria-label="Photo of Spicy Garlic Eggplant" style="background:radial-gradient(circle,#5a2a4a 30%,#e6e2dc 58%,#222222 75%)"></div>
    <div class="info"><h2>Spicy Garlic Eggplant <svg class="chili"><use href="#chili"/></svg></h2><p>Chinese eggplant in spicy garlic sauce garnished with scallions</p></div>
    <div class="price">$10</div>
  </article>
  <article class="item">
    <div class="thumb" role="img" aria-label="Photo of Stir Fried Eggplant" style="background:radial-gradient(circle,#6a3a6a 30%,#9aa0a8 58%,#d8d4ce)"></div>
    <div class="info"><h2>Stir Fried Eggplant <svg class="chili"><use href="#chili"/></svg></h2><p>Chinese eggplant with sautéed green beans</p></div>
    <div class="price">$10</div>
  </article>
  <article class="item">
    <div class="thumb" role="img" aria-label="Photo of Shiitake Baby Bok Choy" style="background:radial-gradient(circle,#6aa04a 30%,#ece8e2 58%,#2a2a2a 76%)"></div>
    <div class="info"><h2 class="plain">Shiitake Baby Bok Choy</h2><p>Sautéed baby bok-choy with Shiitake mushrooms in brown sauce</p></div>
    <div class="price">$10</div>
  </article>
</section>
</body>
</html>
```